Contemporary update for a market leader in foodservice distribution

KORVELT is a market leader in foodservice distribution nationwide.
We have recently adopted a new look and feel for our flagship foodservice rewards programme, and we're looking to have our business cards reflect our new aesthetic. Below is a link to our new rewards website to give you a general idea on the look we're after. https://korveltperks.com.au/

Industry/Entity Type

Distribution

Contact Information for Business Card

Must have space for contact name, position, company name and ABN, address, phone number and direct number, fax, email, and web address.

Font styles to use
Serif
Sans Serif

Requirements
Must have
• We'd like a landscape design, with our 'Tip of the Peak' logo incorporated on either the front or the back of the card. The overall design should be contemporary and professional.
Nice to have
• I have included both the full colour and white version of our company logo - our preference is to have the company logo one solid colour (white, or a shade of grey) although we're also open to designs including the full colour logo. If you are able to incorporate a small Facebook and LinkedIn logo, please do so.
Should not have
• Should not have an over-complicated design. No images of globes, or food.

```html
<!DOCTYPE html>
<html lang="en">
<head>
<meta charset="utf-8">
<title>KORVELT Business Card</title>
<link href="https://fonts.googleapis.com/css2?family=Josefin+Sans:wght@300;400;600&display=swap" rel="stylesheet">
<style>
  :root {
    --page: #e6ebe8;
    --band: #3c3c3e;
    --green: #1fb35c;
    --green-light: #3cc26f;
    --green-dark: #179a4d;
    --ink: #16321f;
    --white: #ffffff;
    --badge: #f2f2ef;
    --wordmark-dark: #2a2a2a;
  }
  * { box-sizing: border-box; margin: 0; padding: 0; }
  html, body { width: 1200px; height: 1000px; overflow: hidden; }
  body {
    background: var(--page);
    font-family: "Josefin Sans", "Helvetica Neue", Arial, sans-serif;
    display: flex;
    align-items: center;
    justify-content: center;
    gap: 40px;
  }
  .card {
    position: relative;
    width: 540px;
    height: 310px;
    overflow: hidden;
    background: var(--band);
    box-shadow: 0 10px 24px rgba(0,0,0,0.18);
  }
  .card__field {
    position: absolute;
    left: 0; top: 42px;
    width: 540px; height: 226px;
    background: radial-gradient(ellipse at 70% 30%, var(--green-light) 0%, var(--green) 55%, var(--green-dark) 100%);
  }
  .card__notch {
    position: absolute;
    left: 0; top: 0;
    width: 540px; height: 310px;
  }
  /* front */
  .badge {
    position: absolute;
    left: 50%; top: 50%;
    width: 172px; height: 172px;
    transform: translate(-50%, -50%);
    border-radius: 50%;
    background: var(--badge);
    border: 4px solid var(--green-dark);
    display: flex;
    align-items: center;
    justify-content: center;
    text-align: center;
  }
  .badge__name {
    font-weight: 600;
    font-size: 26px;
    line-height: 1.05;
    color: var(--wordmark-dark);
  }
  /* back */
  .brand {
    position: absolute;
    left: 38px; top: 78px;
    display: flex;
    align-items: center;
    gap: 10px;
  }
  .brand__dot {
    width: 30px; height: 30px;
    border-radius: 50%;
    background: var(--white);
  }
  .brand__name {
    font-weight: 300;
    font-size: 36px;
    letter-spacing: 1px;
    color: var(--white);
    line-height: 1;
  }
  .brand__tagline {
    position: absolute;
    left: 78px; top: 116px;
    font-size: 6px;
    letter-spacing: 0.5px;
    color: var(--white);
    text-transform: uppercase;
  }
  .company {
    position: absolute;
    left: 78px; top: 140px;
    font-weight: 300;
    font-size: 20px;
    letter-spacing: 0.5px;
    color: var(--ink);
  }
  .contact {
    position: absolute;
    left: 60px; top: 172px;
    list-style: none;
  }
  .contact li, .social li {
    display: flex;
    align-items: center;
    gap: 8px;
    font-size: 9px;
    color: var(--white);
    height: 17px;
  }
  .contact svg, .social svg { width: 10px; height: 10px; flex: none; }
  .social {
    position: absolute;
    left: 320px; top: 62px;
    list-style: none;
  }
</style>
</head>
<body>

  <section class="card card--front" aria-label="Card front">
    <div class="card__field" role="img" aria-label="Green field with flowing lighter green swirl pattern"></div>
    <svg class="card__notch" viewBox="0 0 540 310" aria-hidden="true">
      <polygon points="255,42 270,30 285,42" fill="var(--green)"/>
      <polygon points="255,268 270,280 285,268" fill="var(--green)"/>
    </svg>
    <div class="badge">
      <span class="badge__name">Tip of<br>the Peak</span>
    </div>
  </section>

  <section class="card card--back" aria-label="Card back">
    <div class="card__field" role="img" aria-label="Green field with flowing lighter green swirl pattern"></div>
    <svg class="card__notch" viewBox="0 0 540 310" aria-hidden="true">
      <polygon points="255,42 270,30 285,42" fill="var(--green)"/>
      <polygon points="255,268 270,280 285,268" fill="var(--green)"/>
    </svg>

    <div class="brand">
      <span class="brand__dot"></span>
      <span class="brand__name">KORVELT</span>
    </div>
    <p class="brand__tagline">Nationwide Foodservice Distribution</p>

    <h2 class="company">COMPANY NAME</h2>

    <ul class="contact">
      <li>
        <svg viewBox="0 0 10 10"><rect x="0.5" y="2" width="9" height="6" fill="none" stroke="var(--ink)"/><polyline points="0.5,2 5,5.5 9.5,2" fill="none" stroke="var(--ink)"/></svg>
        PO Box 000
      </li>
      <li>
        <svg viewBox="0 0 10 10"><path d="M2 1 L4 3 L3 4.5 Q4.5 6.5 5.5 7 L7 6 L9 8 L7.5 9.5 Q3 8.5 0.5 2.5 Z" fill="var(--ink)"/></svg>
        000-000-0000
      </li>
      <li>
        <svg viewBox="0 0 10 10"><circle cx="5" cy="5" r="4.2" fill="none" stroke="var(--ink)"/><circle cx="5" cy="5" r="1.8" fill="none" stroke="var(--ink)"/></svg>
        yourname@yourwebsite.com
      </li>
      <li>
        <svg viewBox="0 0 10 10"><polygon points="5,1 9.5,5 8,5 8,9 2,9 2,5 0.5,5" fill="var(--ink)"/></svg>
        www.yourwebsite.com
      </li>
    </ul>

    <ul class="social">
      <li>
        <svg viewBox="0 0 10 10"><path d="M5 0.5 A3.2 3.2 0 0 1 8.2 3.7 C8.2 6 5 9.5 5 9.5 C5 9.5 1.8 6 1.8 3.7 A3.2 3.2 0 0 1 5 0.5 Z" fill="var(--ink)"/><circle cx="5" cy="3.7" r="1.2" fill="var(--green)"/></svg>
        Download/XXXXXX
      </li>
      <li>
        <svg viewBox="0 0 10 10"><circle cx="5" cy="5" r="4" fill="var(--ink)"/></svg>
        facebook.com/username
      </li>
      <li>
        <svg viewBox="0 0 10 10"><circle cx="5" cy="5" r="4" fill="var(--ink)"/></svg>
        linkedin.com/company/companyname
      </li>
    </ul>
  </section>

</body>
</html>
```